Business Card Design

We need a business card designed to the point of print ready to take to our printers. the design should be professional, easy to read and simple. The cards should represent our business as professional and trust worthy.

Attached are several versions o the logo, and also the details for the card to be printed. please do communicate if different versions of the logo is required.

Industry/Entity Type

Business

```html
<!DOCTYPE html>
<html lang="en">
<head>
<meta charset="utf-8">
<title>Brinley Hart Recovery Business Card</title>
<link rel="stylesheet" href="https://fonts.googleapis.com/css2?family=Roboto+Condensed:wght@400;700&display=swap">
<style>
  :root {
    --paper: #ffffff;
    --surround: #1e1d1a;
    --accent: #f39a12;
    --ink-dark: #232323;
    --ink-grey: #666666;
    --brand-grey: #707070;
  }
  html, body {
    margin: 0;
    padding: 0;
    width: 1200px;
    height: 1000px;
    overflow: hidden;
    background: var(--paper);
    font-family: "Roboto Condensed", "Arial Narrow", sans-serif;
  }
  .stage {
    position: absolute;
    left: 18px;
    top: 18px;
    width: 1164px;
    height: 964px;
    background: var(--surround);
  }
  .card {
    position: absolute;
    left: 98px;
    top: 175px;
    width: 1004px;
    height: 650px;
    background: var(--paper);
  }
  .brand {
    position: absolute;
    right: 87px;
    top: 88px;
    text-align: right;
    color: var(--brand-grey);
    font-size: 60px;
    font-weight: 700;
    line-height: 1;
    white-space: nowrap;
  }
  .person {
    position: absolute;
    left: 89px;
    top: 496px;
  }
  .person-name {
    font-size: 31px;
    font-weight: 700;
    color: var(--ink-dark);
    line-height: 36px;
  }
  .person-role {
    font-size: 22px;
    color: var(--ink-grey);
    line-height: 28px;
  }
  .contact {
    position: absolute;
    left: 405px;
    top: 407px;
    margin: 0;
    padding: 0;
    list-style: none;
    font-size: 27px;
    color: var(--ink-grey);
    line-height: 40px;
    white-space: nowrap;
  }
  .contact-label {
    display: inline-block;
    color: var(--accent);
    font-weight: 700;
    min-width: 26px;
  }
  .contact-sep { margin-right: 8px; }
  .accent-band {
    position: absolute;
    left: 0;
    bottom: 0;
    width: 100%;
    height: 55px;
    background: var(--accent);
  }
</style>
</head>
<body>
  <div class="stage"></div>
  <section class="card">
    <div class="brand">Brinley Hart Recovery</div>

    <div class="person">
      <div class="person-name">Joanne Rellick</div>
      <div class="person-role">Managing Director</div>
    </div>

    <ul class="contact">
      <li>PO Box 4120 Harbour Centre Qld 4217</li>
      <li><span class="contact-label">p</span><span class="contact-sep">:</span>+61 400 555 019</li>
      <li><span class="contact-label">e</span><span class="contact-sep">:</span>jrellick@brinleyhart.com.au</li>
      <li><span class="contact-label">w</span><span class="contact-sep">:</span>www.brinleyhart.com.au</li>
    </ul>

    <div class="accent-band"></div>
  </section>
</body>
</html>
```